LUMEN Environmental needs an upgrade to its current business cards design

We need an upgrade to our current business cards design, where the LUMEN acronym is included, as possible and not being overloaded.
LUMEN Environmental is an Environmental Consultancy Firm based in Sydney.
We would like to see creative designs different from the standard type of business cards (for example, rounded edges, different to standard size of common business cards.

Target Market(s)

industrial companies (oil & gas, petrochemical, mining, insolvency, finance and manufacturing), developers, architect firms, law firms.

Industry/Entity Type

Business

Contact Information for Business Card

logos (brand and acronym), if they don't appear overloaded.
name
role
name of company (LUMEN Environmental),
address (Level 4, Suite 4B, 72-76 Wrenfield Street, Marlow Vale, NSW, 2093) landline (02 7314 2286)
mobile (staff member)
email (staff member) and
website (www.lumenverda.example).
Include: Contaminated Land, Site Remediation, Groundwater Assessment, Health and Ecological Risk Assessments, Acid Sulfate Soils, Waste Classification.

Font styles to use
Serif
Sans Serif

Requirements
Must have
• A creative design different to the standard type of business cards.
Nice to have
• Rounded edges
• Different size of business cards rather than the standard size.
Should not have
• Preferable not to use white colour background, unless it is required from a creative design proposed.
• Not an overloaded design.
• Avoid black colours

```html
<!DOCTYPE html>
<html lang="en">
<head>
<meta charset="utf-8">
<title>LUMEN Environmental – Business Cards</title>
<link rel="stylesheet" href="https://fonts.googleapis.com/css2?family=Roboto:wght@400;500;700&display=swap">
<style>
  :root {
    --backdrop: #e6e6e6;
    --green: #8cc21c;
    --green-deep: #7fb418;
    --paper: #f1f4ea;
    --paper-shade: #e6eadc;
    --ink: #5a5a5a;
    --ink-soft: #6a6a6a;
    --band-grey: #6b6b6b;
    --white: #ffffff;
    --white-soft: rgba(255, 255, 255, 0.88);
  }
  * { box-sizing: border-box; margin: 0; padding: 0; }
  html, body {
    width: 1200px; height: 576px; overflow: hidden;
    background: var(--backdrop);
    font-family: "Roboto", Arial, sans-serif;
  }
  .canvas { position: relative; width: 1200px; height: 576px; }

  .card {
    position: absolute; top: 138px; width: 484px; height: 294px;
    border-radius: 8px; overflow: hidden;
  }
  .card--front {
    left: 82px;
    background: linear-gradient(180deg, var(--green) 0%, var(--green-deep) 100%);
  }
  .card--back {
    left: 602px;
    background: linear-gradient(180deg, var(--paper) 0%, var(--paper-shade) 100%);
  }

  .brand { position: absolute; font-weight: 700; line-height: 1; }
  .brand__name { display: block; letter-spacing: 1px; }
  .brand__sub { display: block; letter-spacing: 3.2px; }

  .card--front .brand {
    color: var(--white); left: 0; right: 0; top: 116px; text-align: center;
  }
  .card--front .brand__name { font-size: 46px; }
  .card--front .brand__sub { font-size: 14.5px; margin-top: 6px; padding-left: 14px; }

  .services {
    position: absolute; left: 30px; right: 30px; bottom: 22px;
    list-style: none; text-align: center;
    color: var(--white-soft); font-size: 10.5px; line-height: 16px;
  }
  .services li { display: inline; }
  .services li + li::before { content: "·"; margin: 0 6px; }

  .card--back .brand { color: var(--ink-soft); left: 26px; top: 30px; }
  .card--back .brand__name { font-size: 44px; }
  .card--back .brand__sub { font-size: 14px; margin-top: 6px; letter-spacing: 2.6px; padding-left: 10px; }

  .person { position: absolute; left: 26px; top: 151px; color: var(--ink); }
  .person__name { font-size: 19.5px; font-weight: 500; }
  .person__role { font-size: 12px; margin-top: 5px; color: var(--ink-soft); }

  .contact { position: absolute; list-style: none; color: var(--ink-soft); font-size: 12.8px; }
  .contact li { display: flex; align-items: flex-start; line-height: 17.6px; }
  .contact svg { width: 11px; height: 11px; margin: 3px 9px 0 0; flex: none; fill: var(--green); }
  .contact--personal { left: 26px; top: 211px; }
  .contact--office { left: 290px; top: 163px; }

  .band { position: absolute; left: 0; bottom: 0; width: 100%; height: 12px; }
</style>
</head>
<body>
<main class="canvas">

  <section class="card card--front" aria-label="Card front">
    <div class="brand">
      <span class="brand__name">LUMEN</span>
      <span class="brand__sub">ENVIRONMENTAL</span>
    </div>
    <ul class="services">
      <li>Contaminated Land</li>
      <li>Site Remediation</li>
      <li>Groundwater Assessment</li>
      <li>Health and Ecological Risk Assessments</li>
      <li>Acid Sulfate Soils</li>
      <li>Waste Classification</li>
    </ul>
  </section>

  <section class="card card--back" aria-label="Card back">
    <div class="brand">
      <span class="brand__name">LUMEN</span>
      <span class="brand__sub">ENVIRONMENTAL</span>
    </div>

    <div class="person">
      <p class="person__name">Owen Marlowe</p>
      <p class="person__role">Project Engineer</p>
    </div>

    <ul class="contact contact--personal">
      <li>
        <svg viewBox="0 0 12 12" aria-hidden="true"><path d="M3 0h6a1 1 0 0 1 1 1v10a1 1 0 0 1-1 1H3a1 1 0 0 1-1-1V1a1 1 0 0 1 1-1zm.8 1.5v7.5h4.4V1.5zM6 9.8a.7.7 0 1 0 0 1.4.7.7 0 0 0 0-1.4z"/></svg>
        0412 587 336
      </li>
      <li>
        <svg viewBox="0 0 12 12" aria-hidden="true"><path d="M0 2.5h12v7H0zM1 3.3 6 6.8l5-3.5z" fill-rule="evenodd"/></svg>
        owen@lumenverda.example
      </li>
    </ul>

    <ul class="contact contact--office">
      <li>
        <svg viewBox="0 0 12 12" aria-hidden="true"><path d="M1 3.5C1 2 3 1.2 6 1.2S11 2 11 3.5v1H8.6V3.4H3.4v1.1H1zM3 5.5h6l1.5 5H1.5z"/></svg>
        02 7314 2286
      </li>
      <li>
        <svg viewBox="0 0 12 12" aria-hidden="true"><path d="M6 0a4 4 0 0 1 4 4c0 3-4 8-4 8S2 7 2 4a4 4 0 0 1 4-4zm0 2.4a1.6 1.6 0 1 0 0 3.2 1.6 1.6 0 0 0 0-3.2z"/></svg>
        <span>Level 4, Suite 4B,<br>72-76 Wrenfield Street,<br>Marlow Vale, NSW, 2093</span>
      </li>
      <li>
        <svg viewBox="0 0 12 12" aria-hidden="true"><path d="M6 1a5 5 0 1 0 0 10A5 5 0 0 0 6 1zm-.6 1.2v2.2H3.2A4 4 0 0 1 5.4 2.2zm1.2 0a4 4 0 0 1 2.2 2.2H6.6zM2.1 5.5h3.3v1H2.1zm4.5 0h3.3v1H6.6zM3.2 7.6h2.2v2.2A4 4 0 0 1 3.2 7.6zm3.4 0h2.2a4 4 0 0 1-2.2 2.2z"/></svg>
        www.lumenverda.example
      </li>
    </ul>

    <svg class="band" viewBox="0 0 484 12" preserveAspectRatio="none" aria-hidden="true">
      <polygon points="0,0 335,0 311,12 0,12" fill="var(--green)"/>
      <polygon points="335,0 484,0 484,12 311,12" fill="var(--band-grey)"/>
    </svg>
  </section>

</main>
</body>
</html>
```